Product Box packaging design for CBD Candy Company

We need a complete product box design (dieline template included in zip file) for an online-based CBD Candy product. The Company, Harrowgate Sweets, will be marketing to a mature online audience through a well-established influencer, who focuses on ASMR. We will provide detailed information as to what will be needed on each side of the product box, but need help with the aesthetic aspect of the packaging. We would like to focus on soothing/calming colors and pull in an organic/ nature aspect. The company is based in Tennessee. We will provide a color palette that will mimic the colors of the website as well. Please refer to the zip-file for all specifications.

Target Market(s)

Online subsribers to an established Influencer

Industry/Entity Type

CBD candy industry

Requirements
Must have
• Please follow the dieline template for sizing. The box is 3.5"x3.5"X1.75"
Nice to have
• We want classic, calming, with a nature/rustic and simple feel if possible

```html
<!DOCTYPE html>
<html lang="en">
<head>
<meta charset="utf-8">
<title>Harrowgate Sweets – CBD-Infused Sea Salted Caramels Box</title>
<link href="https://fonts.googleapis.com/css2?family=Barlow:ital,wght@0,400;0,500;0,700;0,800;1,400&family=Barlow+Condensed:wght@600;700;800&display=swap" rel="stylesheet">
<style>
  :root {
    --bg: #f3f3f1;
    --butter: #f2d16f;
    --butter-shade: #e6c462;
    --navy: #0d3554;
    --teal: #1a9cc4;
    --pine: #4e8a6a;
    --olive: #b4bd6a;
    --alert-red: #d9262c;
    --white: #ffffff;
  }
  * { box-sizing: border-box; margin: 0; padding: 0; }
  html, body { width: 1200px; height: 675px; overflow: hidden; background: var(--bg); }
  body { font-family: "Barlow", Arial, sans-serif; color: var(--navy); }

  .dieline {
    position: absolute; left: 70px; top: 110px;
    width: 1060px; height: 455px;
    display: flex; overflow: hidden;
  }
  .panel { position: relative; height: 100%; }
  .panel--front { width: 620px; background: var(--butter); }
  .panel--side { width: 440px; background: var(--butter-shade); }

  .landscape-band {
    position: absolute; left: 0; bottom: 0; width: 1060px; height: 160px;
    background: linear-gradient(180deg,
      var(--olive) 0%, var(--pine) 18%, var(--teal) 32%, var(--navy) 46%, var(--navy) 100%);
  }

  /* Front panel */
  .brand-mark {
    position: absolute; top: 22px; left: 0; width: 100%;
    display: flex; align-items: center; justify-content: center; gap: 14px;
  }
  .brand-mark__dot { width: 34px; height: 34px; border-radius: 50%; background: var(--navy); }
  .brand-mark__name {
    font-family: "Barlow Condensed", "Arial Narrow", sans-serif;
    font-weight: 700; font-size: 40px; letter-spacing: 4px; text-transform: uppercase;
  }

  .product-title { position: absolute; top: 88px; left: 0; width: 100%; text-align: center; }
  .product-title__kicker {
    font-family: "Barlow Condensed", "Arial Narrow", sans-serif;
    font-weight: 800; font-size: 24px; letter-spacing: 0.5px; text-transform: uppercase;
  }
  .product-title__name {
    font-family: "Barlow Condensed", "Arial Narrow", sans-serif;
    font-weight: 800; font-size: 58px; line-height: 0.95; letter-spacing: 5px; text-transform: uppercase;
  }
  .dosage {
    margin: 6px auto 0; width: 330px; border-top: 2px solid var(--navy);
    display: flex; justify-content: space-between; padding-top: 4px;
  }
  .dosage__item { text-align: left; line-height: 1; }
  .dosage__item + .dosage__item { border-left: 2px solid var(--navy); padding-left: 22px; }
  .dosage__amount { font-weight: 700; font-size: 17px; }
  .dosage__unit { font-size: 14px; font-weight: 400; }

  .origin-line {
    position: absolute; top: 250px; left: 0; width: 100%;
    display: flex; align-items: center; justify-content: center; gap: 14px;
    font-weight: 700; font-size: 14px; letter-spacing: 2.5px; text-transform: uppercase;
  }
  .origin-line__brand { display: flex; align-items: center; gap: 6px; font-family: "Barlow Condensed", "Arial Narrow", sans-serif; font-size: 17px; letter-spacing: 1.5px; }
  .origin-line__dot { width: 16px; height: 16px; border-radius: 50%; background: var(--navy); }

  .warning {
    position: absolute; left: 24px; bottom: 16px; width: 566px;
    color: var(--white); font-size: 7.5px; line-height: 1.35;
  }
  .warning p + p { margin-top: 3px; }
  .warning strong { font-weight: 700; }

  /* Side panel */
  .thc-badge {
    position: absolute; top: 24px; right: 28px;
    width: 38px; height: 38px; border: 2px solid var(--alert-red); background: var(--white);
    transform: rotate(45deg);
    display: flex; align-items: center; justify-content: center;
  }
  .thc-badge__label {
    transform: rotate(-45deg);
    color: var(--alert-red); font-weight: 700; font-size: 9px; line-height: 1; text-align: center;
  }
  .side-copy { position: absolute; top: 92px; left: 34px; right: 34px; text-align: center; }
  .side-copy__title {
    font-family: "Barlow Condensed", "Arial Narrow", sans-serif;
    font-weight: 800; font-size: 30px; letter-spacing: 1px; text-transform: uppercase;
  }
  .side-copy__tagline { font-size: 12px; font-style: italic; margin-bottom: 10px; }
  .side-copy__body { font-size: 13.5px; line-height: 1.4; }
  .side-copy__body strong { font-weight: 700; }
</style>
</head>
<body>
  <main class="dieline" aria-label="Harrowgate Sweets caramel box, front and side panels">
    <section class="panel panel--front">
      <div class="brand-mark">
        <span class="brand-mark__dot"></span>
        <span class="brand-mark__name">Harrowgate Sweets</span>
      </div>

      <div class="product-title">
        <p class="product-title__kicker">CBD-Infused Sea Salted</p>
        <h1 class="product-title__name">Caramels</h1>
        <div class="dosage">
          <p class="dosage__item"><span class="dosage__amount">35 mg CBD</span><br><span class="dosage__unit">per Caramel</span></p>
          <p class="dosage__item"><span class="dosage__amount">420 mg</span><br><span class="dosage__unit">per Box</span></p>
        </div>
      </div>

      <div class="origin-line">
        <span>From your friends in</span>
        <span class="origin-line__brand"><span class="origin-line__dot"></span>Harrowgate Sweets</span>
        <span>Nashville, Tennessee</span>
      </div>
    </section>

    <section class="panel panel--side">
      <span class="thc-badge" aria-label="THC warning symbol"><span class="thc-badge__label">!<br>THC</span></span>
      <div class="side-copy">
        <h2 class="side-copy__title">CBD Candies</h2>
        <p class="side-copy__tagline">Southern Artisan CBD Candies</p>
        <p class="side-copy__body">Handcrafted in <strong>Nashville, Tennessee</strong> each batch of our sea salted caramels is perfectly seasoned for the ultimate flavor experience and infused with <strong>premium CO2</strong> extracted full spectrum CBD oil for the perfect blend of <strong>taste and tranquility.</strong></p>
      </div>
    </section>

    <div class="landscape-band" role="img" aria-label="Layered rolling hills and river landscape in olive, green, blue and navy"></div>

    <div class="warning">
      <p><strong>Warning:</strong> This product is not intended for use by any persons under the age of 21. Keep out of the reach of children. Do not consume this product if you are pregnant, at risk of becoming pregnant, or nursing. Do not drive or operate heavy machinery after use.</p>
      <p>It is recommended to consume no more than 2 caramels per day. Allow time between servings; one hour is recommended.</p>
      <p>This product has not been evaluated by the Food and Drug Administration and is not intended to diagnose, treat, cure or prevent any disease. Contains less than 0.3% THC by dry weight.</p>
    </div>
  </main>
</body>
</html>
```